Need 2 sided card for Loomfield Goods Co. Logo supplied.

I am looking for a business card for my online craft supply business.

I have a very simple design already which I am kind of happy with (see attached pdf) - but would like suggestions for something a little more creative. Design MUST be clean. Super clean! Think thin lines and not blocks of color...

Design must be clean and crisp. No other colors other than in palette (see link below)

I would also like to possible incorporate my tagline - maybe on the front but definitely on the back:
"HobbyNest Ideas & Making Materials"

Logo file is supplied, but I think spacing on the card may required the wording to be moved underneaths the camera icon - which is fine. Font in logo is Maven Pro. OPEN TO USE OF OTHER FONTS ON CARD BUT MUST BE CLEAN DESIGN.

FRONT OF CARD
All information on attached pdf is correct and should be shown in your design.

BACK OF CARD
Needs to show www.tinselbrookstore.com and maybe logo repeat and tagline.

SIZE
New Zealand sized - meaning finished card will be 90 x 55mm
Printing requirements: printed area is 90mm x 55mm with a 2mm bleed all round.

COLORS
Color palette used in logo can be seen here for HEX and RGB reference: http://www.huegatherly.net/palette/8802417/website

NOTE: PAYMENT WILL BE MADE FOR THE BEST DESIGN - EVEN IF I DECIDE NOT TO USE IT.
Updates

Thank you all so much for your designs. I will be providing feedback to ALL designers tomorrow. This weekend is a holiday weekend here in New Zealand and so no work for a few days. Thank-you again - I appreciate your time and creativity!

Industry/Entity Type

Camera

Font styles to use
Other font styles liked:
• Maven Pro - open to others

Requirements
Must have
• Clean design. Logo must be prominent for brand recognition. All contact information must be shown.
Nice to have
• Tagline - at least on reverse

```html
<!DOCTYPE html>
<html lang="en">
<head>
<meta charset="utf-8">
<title>Loomfield Goods Co. – Business Card</title>
<link href="https://fonts.googleapis.com/css2?family=Maven+Pro:wght@400;500;700&display=swap" rel="stylesheet">
<style>
  :root {
    --backdrop: #6e4f38;
    --card: #ffffff;
    --charcoal: #58534f;
    --lime: #c9c31c;
    --lime-pale: #efeccb;
    --orange: #e8643a;
    --teal: #4f9a93;
    --text: #4a4643;
  }
  * { margin: 0; padding: 0; box-sizing: border-box; }
  html, body { width: 1200px; height: 418px; overflow: hidden; }
  body {
    background: var(--backdrop);
    font-family: "Maven Pro", sans-serif;
    position: relative;
  }
  .card {
    position: absolute;
    top: 68px;
    width: 468px;
    height: 288px;
    background: var(--card);
    overflow: hidden;
    box-shadow: 0 2px 6px rgba(0,0,0,0.35);
  }
  .card--front { left: 120px; }
  .card--back { left: 619px; }

  .front-swoosh { position: absolute; inset: 0; }

  .holder-name {
    position: absolute; right: 24px; top: 30px;
    font-size: 19px; font-weight: 700; color: var(--lime);
  }
  .holder-site {
    position: absolute; right: 24px; top: 56px;
    font-size: 12px; font-weight: 500; color: #ffffff;
  }

  .brand-mark {
    position: absolute; border-radius: 50%; background: var(--charcoal);
  }
  .brand-name {
    position: absolute; color: var(--charcoal); font-weight: 400; white-space: nowrap;
  }
  .card--front .brand-mark { left: 78px; top: 46px; width: 58px; height: 58px; }
  .card--front .brand-name { left: 24px; top: 118px; font-size: 24px; }

  .contact-list {
    position: absolute; left: 24px; top: 190px; list-style: none;
  }
  .contact-list li {
    display: flex; align-items: center; gap: 9px;
    font-size: 11px; line-height: 15.5px; color: var(--text);
  }
  .contact-dot {
    width: 10px; height: 10px; border-radius: 50%; flex: none;
    display: flex; align-items: center; justify-content: center;
  }
  .dot-phone { background: var(--orange); }
  .dot-mobile { background: var(--lime); }
  .dot-email { background: var(--teal); }
  .dot-social { background: var(--charcoal); }
  .dot-web { background: var(--teal); }

  .faint-mark {
    position: absolute; left: 330px; top: 168px;
    width: 76px; height: 76px; border-radius: 50%; background: var(--lime-pale);
  }
  .front-tagline {
    position: absolute; left: 290px; top: 248px; width: 160px;
    text-align: center; font-size: 11px; font-weight: 700; line-height: 14px;
    color: var(--text);
  }

  .card--back .brand-mark { left: 198px; top: 70px; width: 72px; height: 72px; }
  .card--back .brand-name { left: 0; width: 468px; text-align: center; top: 158px; font-size: 30px; }
  .back-tagline {
    position: absolute; left: 0; width: 468px; top: 236px;
    text-align: center; font-size: 15px; color: var(--text);
  }
</style>
</head>
<body>
  <section class="card card--front">
    <svg class="front-swoosh" width="468" height="288" viewBox="0 0 468 288">
      <path d="M108 0 C280 30 420 140 468 288 L468 262 C420 140 300 34 150 0 Z" fill="var(--lime)"/>
      <path d="M150 0 L468 0 L468 262 C420 140 300 34 150 0 Z" fill="var(--charcoal)"/>
    </svg>
    <p class="holder-name">Maren Holloway</p>
    <p class="holder-site">www.loomfieldnz.com</p>

    <span class="brand-mark"></span>
    <p class="brand-name">Loomfield Goods Co.</p>

    <ul class="contact-list">
      <li>
        <span class="contact-dot dot-phone">
          <svg width="6" height="6" viewBox="0 0 10 10"><path d="M2 1 L4 1 L4.5 3 L3.3 4 Q4.5 6 6 6.7 L7 5.5 L9 6 L9 8 Q5 9 2.5 6.5 Q0.8 4 2 1 Z" fill="#fff"/></svg>
        </span>+64 (0) 3 555 0142
      </li>
      <li><span class="contact-dot dot-mobile"></span>+64 (0) 21 555 01837</li>
      <li><span class="contact-dot dot-email"></span>maren.holloway@loomfieldnz.com</li>
      <li><span class="contact-dot dot-social"></span>chatterloop.com/loomfield</li>
      <li><span class="contact-dot dot-web"></span>www.tinselbrookstore.com</li>
    </ul>

    <span class="faint-mark"></span>
    <p class="front-tagline">HobbyNest Ideas<br>&amp; Making Materials</p>
  </section>

  <section class="card card--back">
    <span class="brand-mark"></span>
    <p class="brand-name">Loomfield Goods Co.</p>
    <p class="back-tagline">HobbyNest Ideas &amp; Making Materials</p>
  </section>
</body>
</html>
```